App Design for quiz app (casual gaming app)

We need an design & logo for our quiz app. Its a simple quiz app, where you pick up a category, answer three questions out of this category. After this an opponent is assigned to your game, and has to answer the same three questions. After this first round is finished, it's the opponents turn to choose a new category and answer three questions out of this category. Now it's your turn to answer the same three questions. With this done, the 2nd round is finished. One game has seven rounds.
Please find attached the balsamiq project. For all of you, do not have balsamiq, please find also the mockups as pdf.
Final delivery should be psd files
Target Market(s)
Casual Games

```html
<!DOCTYPE html>
<html lang="en">
<head>
<meta charset="utf-8">
<title>Quizling – Game Overview</title>
<link rel="stylesheet" href="https://fonts.googleapis.com/css2?family=Nunito:wght@600;700;800&display=swap">
<style>
  :root {
    --page-bg: #f2f2f2;
    --tile-dark: #24495c;
    --status-bar: #1f4f66;
    --nav-bar: #2c7ea0;
    --screen-bg: #68b2d0;
    --board-bg: #386b94;
    --board-line: #9cc9df;
    --text-light: #ffffff;
    --score-win: #2fd34a;
    --score-lose: #d33a2c;
    --dot-green: #3bb54a;
    --dot-red: #c9352b;
    --button-green: #3bb54a;
  }
  * { box-sizing: border-box; margin: 0; padding: 0; }
  html, body { width: 1200px; height: 800px; overflow: hidden; }
  body {
    background: var(--page-bg);
    font-family: "Nunito", "Helvetica Neue", Arial, sans-serif;
    color: var(--text-light);
    position: relative;
  }

  /* App brand tile */
  .brand-tile {
    position: absolute; left: 175px; top: 258px;
    width: 270px; height: 270px; border-radius: 48px;
    background: var(--tile-dark);
    display: flex; align-items: center; justify-content: center;
  }
  .brand-name { font-size: 44px; font-weight: 800; color: var(--text-light); }

  /* App screen */
  .app-screen {
    position: absolute; left: 615px; top: 110px;
    width: 320px; height: 566px;
    background: var(--screen-bg);
    overflow: hidden;
  }
  .status-bar {
    height: 22px; background: var(--status-bar);
    display: flex; align-items: center; justify-content: space-between;
    padding: 0 10px; font-size: 11px; font-weight: 700;
  }
  .status-left, .status-right { display: flex; align-items: center; gap: 4px; width: 100px; }
  .status-right { justify-content: flex-end; }
  .nav-bar {
    height: 46px; background: var(--nav-bar);
    display: flex; align-items: center; padding-left: 18px;
  }

  .players {
    position: absolute; top: 75px; left: 0; width: 100%; height: 75px;
  }
  .player { position: absolute; width: 80px; text-align: center; font-size: 17px; font-weight: 600; }
  .player-one { left: 40px; }
  .player-two { left: 197px; }
  .avatar {
    display: block; margin: 0 auto 4px;
    width: 46px; height: 46px; border-radius: 50%;
    border: 2px solid var(--text-light);
    background: #4d93b4;
  }
  .score {
    position: absolute; left: 0; width: 100%; top: 14px;
    text-align: center; font-size: 24px; font-weight: 800; letter-spacing: -0.5px;
  }
  .score-win { color: var(--score-win); }
  .score-lose { color: var(--score-lose); }

  .round-board {
    position: absolute; left: 33px; top: 161px;
    width: 252px; height: 302px;
    background: var(--board-bg);
    border: 1px solid var(--board-line); border-radius: 3px;
    padding-top: 13px;
  }
  .round {
    height: 40px; display: flex; align-items: flex-start; justify-content: space-between;
    padding: 0 22px;
  }
  .answers { display: flex; gap: 4px; margin-top: 18px; }
  .answer {
    width: 12px; height: 12px; border-radius: 3px;
    border: 1px solid #c8dceb;
  }
  .answer.correct { background: var(--dot-green); border-color: #d7f0da; }
  .answer.wrong { background: var(--dot-red); border-color: #f0d2cf; }
  .round-label { text-align: center; line-height: 1; }
  .round-title { display: block; font-size: 15px; font-weight: 600; }
  .round-category { display: block; font-size: 10px; font-weight: 600; margin-top: 4px; }

  .resume-button {
    position: absolute; left: 33px; top: 487px;
    width: 253px; height: 37px; border-radius: 3px;
    background: var(--button-green);
    border: 1px solid #c8e9cc;
    display: flex; align-items: center; justify-content: center;
    font-size: 17px; font-weight: 600;
  }
  .resume-button svg { position: absolute; left: 10px; top: 9px; }
</style>
</head>
<body>

  <div class="brand-tile"><span class="brand-name">Quizling</span></div>

  <main class="app-screen">
    <div class="status-bar">
      <div class="status-left">
        <span>●●●○○</span><span>CARRIER</span>
        <svg width="12" height="10" viewBox="0 0 12 10"><path d="M1 3.5a7 7 0 0 1 10 0M3 5.5a4 4 0 0 1 6 0" stroke="#fff" stroke-width="1.4" fill="none"/><circle cx="6" cy="8" r="1.2" fill="#fff"/></svg>
      </div>
      <span>4:21 PM</span>
      <div class="status-right">
        <svg width="7" height="11" viewBox="0 0 7 11"><path d="M1 3l5 5-2.5 2V1L6 3 1 8" stroke="#fff" stroke-width="1" fill="none"/></svg>
        <span>22%</span>
        <svg width="22" height="10" viewBox="0 0 22 10"><rect x="0.5" y="0.5" width="19" height="9" rx="2" stroke="#fff" fill="none"/><rect x="2" y="2" width="4" height="6" fill="#fff"/><rect x="20" y="3" width="1.5" height="4" fill="#fff"/></svg>
      </div>
    </div>

    <nav class="nav-bar">
      <svg width="16" height="12" viewBox="0 0 16 12"><path d="M0 1h16M0 6h16M0 11h16" stroke="#fff" stroke-width="2"/></svg>
    </nav>

    <section class="players">
      <div class="player player-one"><span class="avatar" role="img" aria-label="Player 1 avatar"></span>Player 1</div>
      <div class="score"><span class="score-win">15</span>:<span class="score-lose">13</span></div>
      <div class="player player-two"><span class="avatar" role="img" aria-label="Player 2 avatar"></span>Player 2</div>
    </section>

    <section class="round-board">
      <div class="round">
        <div class="answers"><i class="answer correct"></i><i class="answer correct"></i><i class="answer wrong"></i></div>
        <div class="round-label"><span class="round-title">Round 1</span><span class="round-category">Category</span></div>
        <div class="answers"><i class="answer correct"></i><i class="answer wrong"></i><i class="answer wrong"></i></div>
      </div>
      <div class="round">
        <div class="answers"><i class="answer"></i><i class="answer"></i><i class="answer"></i></div>
        <div class="round-label"><span class="round-title">Round 2</span><span class="round-category">Category</span></div>
        <div class="answers"><i class="answer correct"></i><i class="answer wrong"></i><i class="answer wrong"></i></div>
      </div>
      <div class="round">
        <div class="answers"><i class="answer"></i><i class="answer"></i><i class="answer"></i></div>
        <div class="round-label"><span class="round-title">Round 3</span><span class="round-category">Category</span></div>
        <div class="answers"><i class="answer"></i><i class="answer"></i><i class="answer"></i></div>
      </div>
      <div class="round">
        <div class="answers"><i class="answer"></i><i class="answer"></i><i class="answer"></i></div>
        <div class="round-label"><span class="round-title">Round 4</span><span class="round-category">Category</span></div>
        <div class="answers"><i class="answer"></i><i class="answer"></i><i class="answer"></i></div>
      </div>
      <div class="round">
        <div class="answers"><i class="answer"></i><i class="answer"></i><i class="answer"></i></div>
        <div class="round-label"><span class="round-title">Round 5</span><span class="round-category">Category</span></div>
        <div class="answers"><i class="answer"></i><i class="answer"></i><i class="answer"></i></div>
      </div>
      <div class="round">
        <div class="answers"><i class="answer"></i><i class="answer"></i><i class="answer"></i></div>
        <div class="round-label"><span class="round-title">Round 6</span><span class="round-category">Category</span></div>
        <div class="answers"><i class="answer"></i><i class="answer"></i><i class="answer"></i></div>
      </div>
      <div class="round">
        <div class="answers"><i class="answer"></i><i class="answer"></i><i class="answer"></i></div>
        <div class="round-label"><span class="round-title">Round 7</span><span class="round-category">Category</span></div>
        <div class="answers"><i class="answer"></i><i class="answer"></i><i class="answer"></i></div>
      </div>
    </section>

    <div class="resume-button">
      <svg width="20" height="18" viewBox="0 0 20 18"><path d="M1 9h15M10 2l7 7-7 7" stroke="#fff" stroke-width="3" fill="none" stroke-linejoin="round"/></svg>
      Resume Game
    </div>
  </main>

</body>
</html>
```